Dr K.L. Brennick, Consultant General Surgeon

Modern minimalistic look [shades of blue should be included]
I would like an interactive website which gives information about
1. Home page: office location
Medical Partners
📞(876) 555-0142-7
📱(876) 555-0193
📍27 Larkspur Close, Kingston 10

VeldaMed
1-876-555-0117 / 1-876-555-0168 / 1-876-555-0124
📍45 North Pelham Grove RD, Kingston, Jamaica (Upstairs Brisco Meadowlane)
Info@veldamed-example.com

Crestline Medical Suites
📞(876) 555-0176
📱(876) 555-0158
📍Shop 33-34, Delvin Arcade Shopping Mall, Portmore

Pridmore Medical Centre
📞 (876) 555-0131
📍 9 Quellow Street , May Pen
The office logos will be attached
Booking details on this page or 2nd page with procedures

2. My surgical services . - I will attach a business card with the information for this section - do not upload the actual business card on the site

3. Allow the booking of appointments at any of the offices
4. A section where short explainer videos will be uploaded (this section is titled "Surgery in 3D"- I will upload an example below
5. A section- which shows videos of procedures. This section is titled "Surgical procedures" - I will upload one below
these videos will similar the same as the ones on my Instagram account
Link: https://www.instagram.com/dr_klbrennick?igsh=QXhzYWx0ZXN0cGxh&utm_source=qr

6. Gallery- section with pictures from interviews/ presentations/conferences etc

Each section should be on a different page.
The clearly defined sections can be represented from a HOME PAGE or drop-down menu
SIMILAR websites:
Modern professional design style (fonts and layout)- https://velmorcliniccraft.example
others -- this best captures the style I'm looking for. I prefer if the page is not crowded
https://veldamed-example.com
layered effect -- https://harbinwellplace.example/general-surgeon/
https://drnestorbalfour.example

Target Market(s)

Patients who require general surgical care

Coding

Coded - Design and coding required

Number of Pages Required

5+ page

Requirements
Must have
• Each section should be on a different page.

```html
<!DOCTYPE html>
<html lang="en">
<head>
<meta charset="utf-8">
<title>Dr K.L. Brennick – Consultant General Surgeon</title>
<link href="https://fonts.googleapis.com/css2?family=Montserrat:wght@300;400;500;600;700;800&display=swap" rel="stylesheet">
<style>
:root{
  --blue:#1187d0;
  --blue-bright:#2aa7e2;
  --blue-deep:#0a64ad;
  --blue-card:#3cb0e4;
  --ink:#111;
  --text:#222;
  --pale:#e4f1f8;
  --line:#d6dde2;
  --white:#fff;
}
*{box-sizing:border-box;margin:0;padding:0}
html,body{width:1200px;height:4389px;overflow:hidden}
body{position:relative;font-family:'Montserrat',sans-serif;color:var(--text);background:var(--white)}
.abs{position:absolute}

/* header */
.site-header{left:0;top:0;width:1200px;height:111px}
.brand{left:112px;top:42px;font-size:24px;font-weight:600;color:var(--ink);line-height:1;white-space:nowrap}
.main-nav{left:424px;top:50px;display:flex;font-size:13px;font-weight:600;color:#222}
.main-nav span{margin-right:38px}
.btn-contact{left:977px;top:35px;width:109px;height:42px;border-radius:21px;background:linear-gradient(90deg,var(--blue-bright),var(--blue-deep));color:#fff;font-size:13px;font-weight:700;display:flex;align-items:center;justify-content:center}

/* hero */
.hero-panel{left:0;top:111px;width:625px;height:538px;background:linear-gradient(135deg,#2aa3e0 0%,#0f86d0 55%,#0b79c6 100%);overflow:hidden}
.hero-panel .bubble{position:absolute;border-radius:50%;background:rgba(255,255,255,.13)}
.hero-photo{left:625px;top:111px;width:575px;height:538px;background:linear-gradient(180deg,#d8dde0,#eceff0 60%,#c9cdd0)}
.hero-title{left:123px;top:285px;font-size:44px;font-weight:700;color:#fff;letter-spacing:.5px;white-space:nowrap}
.hero-sub{left:124px;top:347px;font-size:23px;font-weight:300;color:#fff}
.hero-text{left:128px;top:397px;width:420px;font-size:14px;line-height:20px;color:#fff}
.btn-outline{border:2px solid #fff;border-radius:22px;color:#fff;font-size:15px;font-weight:700;display:flex;align-items:center;justify-content:center}
.hero-btn{left:128px;top:464px;width:259px;height:41px}

/* services intro */
.services-photo{left:126px;top:758px;width:472px;height:348px;border-radius:6px;background:linear-gradient(135deg,#0d3e6e,#1b6fa6 55%,#18b0c8)}
.section-title{font-size:32px;font-weight:700;color:var(--ink);line-height:37px;letter-spacing:.3px}
.services-title{left:645px;top:800px}
.services-text{left:647px;top:890px;width:400px;font-size:14.6px;line-height:23px;color:#222}

/* cards */
.list-card{top:1203px;width:307px;height:338px;border:1px solid var(--line);border-radius:8px;overflow:hidden;background:#fff}
.list-card h3{height:70px;background:var(--blue-card);color:#fff;font-size:18px;font-weight:600;display:flex;align-items:center;justify-content:center}
.list-card ul{list-style:none;padding:24px 0 0 38px}
.list-card li{font-size:15px;font-weight:600;height:36px;display:flex;align-items:center;gap:10px;color:#222}
.card-services{left:278px}
.card-offices{left:615px}

/* booking band */
.booking-band{left:0;top:1638px;width:1200px;height:349px;background:linear-gradient(100deg,#1683cf 0%,#1e8fd8 40%,#0d6fbc 75%,#0a5fa8 100%)}
.band-title{left:126px;top:1753px;font-size:30px;font-weight:700;color:#fff}
.band-text{left:126px;top:1803px;width:570px;font-size:14.6px;line-height:23px;color:#fff}
.band-btn{left:813px;top:1798px;width:259px;height:43px}

/* surgery 3d */
.pale-band{left:0;top:1987px;width:1200px;height:570px;background:var(--pale)}
.center-title{left:0;width:1200px;text-align:center;font-size:32px;font-weight:700;color:var(--ink)}
.center-text{left:260px;width:680px;text-align:center;font-size:14.6px;line-height:23px;color:#222}
.video-main{left:128px;top:2284px;width:944px;height:448px;border-radius:8px;background:linear-gradient(110deg,#5c6e7a 0%,#8ea4b0 35%,#3f6ea8 60%,#6fa3d8 100%)}
.play{position:absolute;width:64px;height:64px;border-radius:50%;background:var(--blue);display:flex;align-items:center;justify-content:center}

/* procedures */
.proc-title{left:126px;top:2925px}
.proc-text{left:126px;top:3022px;width:340px;font-size:14.6px;line-height:23.2px;color:#222}
.btn-fill{background:linear-gradient(90deg,var(--blue-bright),var(--blue-deep));color:#fff;font-weight:700;display:flex;align-items:center;justify-content:center}
.proc-btn{left:128px;top:3233px;width:155px;height:41px;border-radius:21px;font-size:15px}
.video-proc1{left:494px;top:2918px;width:459px;height:370px;border-radius:6px;background:linear-gradient(135deg,#3a3a3a,#9a9a9a 50%,#cfcfcf)}
.video-proc2{left:982px;top:2918px;width:218px;height:370px;border-radius:6px 0 0 6px;background:linear-gradient(135deg,#1d4d7e,#3f7cb4 60%,#2a5f92)}

/* form */
.form-field{border:1px solid #bfc5c9;border-radius:4px;font-size:14.6px;color:#222;display:flex;align-items:center;padding:0 15px;background:#fff}
.form-field.tall{align-items:flex-start;padding-top:16px}
.submit{left:510px;top:3850px;width:180px;height:60px;border-radius:30px;font-size:16px}

/* footer */
.site-footer{left:0;top:3930px;width:1200px;height:459px}
.contact-item{top:4101px;display:flex;align-items:center;gap:17px;color:#fff;font-size:14.6px;line-height:18px}
.contact-ico{width:40px;height:40px;border:2px solid #fff;border-radius:50%;display:flex;align-items:center;justify-content:center}
.footer-rule{left:141px;top:4185px;width:918px;height:1px;background:rgba(255,255,255,.35)}
.footer-nav{left:0;top:4236px;width:1200px;display:flex;justify-content:center;gap:38px;font-size:13px;font-weight:700;color:#fff}
.copyright{left:0;top:4306px;width:1200px;text-align:center;font-size:14.6px;color:#fff}
</style>
</head>
<body>

<header class="abs site-header">
  <div class="abs brand">Dr K.L. Brennick</div>
  <nav class="abs main-nav">
    <span>HOME</span><span>ABOUT</span><span>SERVICES</span><span>PROCEDURES</span><span>SURGERY IN 3D</span>
  </nav>
  <div class="abs btn-contact">CONTACT</div>
</header>

<section>
  <div class="abs hero-panel">
    <div class="bubble" style="left:-55px;top:-110px;width:280px;height:280px"></div>
    <div class="bubble" style="left:-55px;top:100px;width:120px;height:120px"></div>
  </div>
  <div class="abs hero-photo" role="img" aria-label="Portrait of the surgeon in a dark suit standing in a hospital corridor"></div>
  <h1 class="abs hero-title">DR K.L. BRENNICK</h1>
  <div class="abs hero-sub">Consultant General Surgeon</div>
  <p class="abs hero-text">Lorem ipsum dolor sit amet, consectetur adipiscing eli sed do eiusmod tempor incididunt ut labores.</p>
  <div class="abs btn-outline hero-btn">BOOK AN APPOINTMENT</div>
</section>

<section>
  <div class="abs services-photo" role="img" aria-label="Surgeons' gloved hands holding surgical instruments over a patient"></div>
  <h2 class="abs section-title services-title">MY SURGICAL SERVICES<br>AND OFFICES</h2>
  <p class="abs services-text">Lorem ipsum dolor sit amet, consectetur adipiscing elit, sed do eiusmod tempor incididunt ut labore et dolore magna aliqua. Quis ipsum suspendisse ultrices gravida. Risus commodo viverra maecenas accumsan lacus vel facilisisLorem ipsum dolor sit amet, consectetur adipiscing elit, sed do eiusmod tempor incididunt ut labore et dolore magna aliqua. Quis ipsum suspendisse ultrices gravida.</p>

  <div class="abs list-card card-services">
    <h3>MY SURGICAL SERVICES</h3>
    <ul>
      <li><svg width="12" height="12" viewBox="0 0 12 12"><circle cx="6" cy="6" r="6" fill="#2aa7e2"/><path d="M3.3 6.2l1.8 1.7 3.6-3.6" stroke="#fff" stroke-width="1.5" fill="none"/></svg>Lorem ipsum dolor simet</li>
      <li><svg width="12" height="12" viewBox="0 0 12 12"><circle cx="6" cy="6" r="6" fill="#2aa7e2"/><path d="M3.3 6.2l1.8 1.7 3.6-3.6" stroke="#fff" stroke-width="1.5" fill="none"/></svg>Wonsectetur adipiscg</li>
      <li><svg width="12" height="12" viewBox="0 0 12 12"><circle cx="6" cy="6" r="6" fill="#2aa7e2"/><path d="M3.3 6.2l1.8 1.7 3.6-3.6" stroke="#fff" stroke-width="1.5" fill="none"/></svg>Praesent cursus sem a lao</li>
      <li><svg width="12" height="12" viewBox="0 0 12 12"><circle cx="6" cy="6" r="6" fill="#2aa7e2"/><path d="M3.3 6.2l1.8 1.7 3.6-3.6" stroke="#fff" stroke-width="1.5" fill="none"/></svg>Rrevet dignissim</li>
      <li><svg width="12" height="12" viewBox="0 0 12 12"><circle cx="6" cy="6" r="6" fill="#2aa7e2"/><path d="M3.3 6.2l1.8 1.7 3.6-3.6" stroke="#fff" stroke-width="1.5" fill="none"/></svg>Curabitur pretiu nisat</li>
      <li><svg width="12" height="12" viewBox="0 0 12 12"><circle cx="6" cy="6" r="6" fill="#2aa7e2"/><path d="M3.3 6.2l1.8 1.7 3.6-3.6" stroke="#fff" stroke-width="1.5" fill="none"/></svg>Sehicula imperdiet</li>
    </ul>
  </div>

  <div class="abs list-card card-offices">
    <h3>OFFICES</h3>
    <ul>
      <li><svg width="10" height="13" viewBox="0 0 10 13"><path d="M5 0a5 5 0 0 1 5 5c0 3.5-5 8-5 8S0 8.5 0 5a5 5 0 0 1 5-5z" fill="#2aa7e2"/><circle cx="5" cy="5" r="1.8" fill="#fff"/></svg>Lorem ipsum dolor simet</li>
      <li><svg width="10" height="13" viewBox="0 0 10 13"><path d="M5 0a5 5 0 0 1 5 5c0 3.5-5 8-5 8S0 8.5 0 5a5 5 0 0 1 5-5z" fill="#2aa7e2"/><circle cx="5" cy="5" r="1.8" fill="#fff"/></svg>Wonsectetur adipiscg</li>
      <li><svg width="10" height="13" viewBox="0 0 10 13"><path d="M5 0a5 5 0 0 1 5 5c0 3.5-5 8-5 8S0 8.5 0 5a5 5 0 0 1 5-5z" fill="#2aa7e2"/><circle cx="5" cy="5" r="1.8" fill="#fff"/></svg>Praesent cursus sem a lao</li>
      <li><svg width="10" height="13" viewBox="0 0 10 13"><path d="M5 0a5 5 0 0 1 5 5c0 3.5-5 8-5 8S0 8.5 0 5a5 5 0 0 1 5-5z" fill="#2aa7e2"/><circle cx="5" cy="5" r="1.8" fill="#fff"/></svg>Rreet dignissim</li>
      <li><svg width="10" height="13" viewBox="0 0 10 13"><path d="M5 0a5 5 0 0 1 5 5c0 3.5-5 8-5 8S0 8.5 0 5a5 5 0 0 1 5-5z" fill="#2aa7e2"/><circle cx="5" cy="5" r="1.8" fill="#fff"/></svg>Curabitur pretiu nisat</li>
      <li><svg width="10" height="13" viewBox="0 0 10 13"><path d="M5 0a5 5 0 0 1 5 5c0 3.5-5 8-5 8S0 8.5 0 5a5 5 0 0 1 5-5z" fill="#2aa7e2"/><circle cx="5" cy="5" r="1.8" fill="#fff"/></svg>Sehicula imperdiet</li>
    </ul>
  </div>
</section>

<section>
  <div class="abs booking-band" role="img" aria-label="Blurred blue-tinted photo of a surgical team in theatre"></div>
  <h2 class="abs band-title">BOOKING AN APPOINTMENTS</h2>
  <p class="abs band-text">Lorem ipsum dolor sit amet, consectetur adipiscing elit, sed do eiusmod tempor incididunt ut labore et dolore magna aliquaipsum suspendisse ultrices gravida. Risus commodo viverra maecenas.</p>
  <div class="abs btn-outline band-btn">BOOK AN APPOINTMENT</div>
</section>

<section>
  <div class="abs pale-band"></div>
  <h2 class="abs center-title" style="top:2078px">SURGERY IN 3D</h2>
  <p class="abs center-text" style="top:2138px">Lorem ipsum dolor sit amet, consectetur adipiscing elit, sed do eiusmod tempor incididunt ut labore et dolore magna aliqua. Quis ipsum suspendisse ultrices gravida. Risus commodo viverra maecenas accumsan lacus vel facilisisLorem ipsum dolor sit amet, consectetur adipiscing elit, sed do eiusmod tempor incididunt ut labore.</p>
  <div class="abs video-main" role="img" aria-label="Video still of a surgical team performing a laparoscopic procedure with a monitor">
    <div class="play" style="left:440px;top:191px"><svg width="20" height="22" viewBox="0 0 20 22"><path d="M2 1l17 10L2 21z" fill="#fff"/></svg></div>
  </div>
</section>

<section>
  <h2 class="abs section-title proc-title">SURGICAL<br>PROCEDURES</h2>
  <p class="abs proc-text">Lorem ipsum dolor sit amet, consectetur adipiscing elit, sed do eiusmod tempor inc ididunt ut labore et dolore magna aliquauis ipsum suspendisse ultrices gravida. Risus commodo viverra maecenas accumsan lac us vel facilisisLorem ipsum dolor sit amet, consectetur adipiscing elit, sed do eiusmod tempor incididunt ut labore.</p>
  <div class="abs btn-fill proc-btn">READ MORE</div>
  <div class="abs video-proc1" role="img" aria-label="Black and white video still of a masked surgeon operating">
    <div class="play" style="left:25px;top:280px"><svg width="20" height="22" viewBox="0 0 20 22"><path d="M2 1l17 10L2 21z" fill="#fff"/></svg></div>
  </div>
  <div class="abs video-proc2" role="img" aria-label="Video still of a surgical team under operating theatre lights">
    <div class="play" style="left:24px;top:280px"><svg width="20" height="22" viewBox="0 0 20 22"><path d="M2 1l17 10L2 21z" fill="#fff"/></svg></div>
  </div>
</section>

<section>
  <h2 class="abs center-title" style="top:3438px">BOOKING AN APPOINTMENT</h2>
  <p class="abs center-text" style="top:3499px">Lorem ipsum dolor sit amet, consectetur adipiscing elit, sed do eiusmod tempor incLorem ipsum dolor sit amet, consectetur adipiscing eli.</p>
  <div class="abs form-field" style="left:213px;top:3568px;width:380px;height:57px">Name:</div>
  <div class="abs form-field" style="left:605px;top:3568px;width:380px;height:57px">Phone:</div>
  <div class="abs form-field" style="left:213px;top:3639px;width:380px;height:58px;justify-content:space-between">Date &amp; Time
    <svg width="14" height="14" viewBox="0 0 14 14"><rect x="1" y="2" width="12" height="11" rx="1" fill="none" stroke="#222" stroke-width="1.5"/><rect x="1" y="2" width="12" height="3" fill="#222"/></svg></div>
  <div class="abs form-field" style="left:605px;top:3639px;width:380px;height:58px;justify-content:space-between">Service Name:
    <svg width="8" height="6" viewBox="0 0 8 6"><path d="M0 0h8L4 6z" fill="#222"/></svg></div>
  <div class="abs form-field tall" style="left:213px;top:3714px;width:772px;height:106px">Message:</div>
  <div class="abs btn-fill submit">SUBMIT NOW</div>
</section>

<footer class="abs site-footer">
  <svg class="abs" style="left:0;top:0" width="1200" height="459" viewBox="0 0 1200 459">
    <defs><linearGradient id="footerGrad" x1="0" y1="0" x2="1" y2="1"><stop offset="0" stop-color="#1592d6"/><stop offset="1" stop-color="#0a6bb3"/></linearGradient></defs>
    <path d="M0 42 C200 120 420 70 620 30 C820 -8 1000 -10 1200 30 L1200 459 L0 459 Z" fill="url(#footerGrad)"/>
  </svg>
</footer>
<div class="abs contact-item" style="left:242px">
  <div class="contact-ico"><svg width="14" height="18" viewBox="0 0 10 13"><path d="M5 0a5 5 0 0 1 5 5c0 3.5-5 8-5 8S0 8.5 0 5a5 5 0 0 1 5-5z" fill="none" stroke="#fff" stroke-width="1.3"/><circle cx="5" cy="5" r="1.6" fill="#fff"/></svg></div>
  <div>Location Name:<br>27 Larkspur Close</div>
</div>
<div class="abs contact-item" style="left:500px">
  <div class="contact-ico"><svg width="18" height="18" viewBox="0 0 24 24"><path d="M6.6 10.8a15 15 0 0 0 6.6 6.6l2.2-2.2a1 1 0 0 1 1-.25 11.4 11.4 0 0 0 3.6.57 1 1 0 0 1 1 1V20a1 1 0 0 1-1 1A17 17 0 0 1 3 4a1 1 0 0 1 1-1h3.5a1 1 0 0 1 1 1c0 1.25.2 2.450.57 3.57a1 1 0 0 1-.25 1z" fill="#fff"/></svg></div>
  <div>Phone:<br>(876) 555-0142-7</div>
</div>
<div class="abs contact-item" style="left:749px">
  <div class="contact-ico"><svg width="16" height="12" viewBox="0 0 16 12"><rect width="16" height="12" rx="1.5" fill="#fff"/><path d="M1 1.5l7 5 7-5" stroke="#0f7ec8" stroke-width="1.4" fill="none"/></svg></div>
  <div>Email:<br>info@brennick-example.com</div>
</div>
<div class="abs footer-rule"></div>
<nav class="abs footer-nav"><span>HOME</span><span>ABOUT</span><span>SERVICES</span><span>PROCEDURES</span><span>SURGERY IN 3D</span><span>CONTACT</span></nav>
<p class="abs copyright">Copyright © 2024 All rights are reserved.</p>

</body>
</html>
```